Facebook & Instagram Ads for Velvet Drift, the world's first device to improve memory throu...

About Us
Velvet Drift® is a revolutionary bedside device that improves memory while you sleep. Backed by groundbreaking clinical research from the Norbrook State University Halvern, our device uses gentle, rotating scents to enhance memory and brian fog naturally. With zero pills, zero side effects, and zero effort, Velvet Drift offers a new path to better memory. www.velvetdrift-example.com

The Challenge
We are looking for bold, imaginative, and highly shareable static and GIF ad designs for Facebook and Instagram. This isn’t just another health device—it’s a category-defining product. Your job is to help us stop the scroll with creative ad concepts that communicate the elegance, science, and life-changing benefits of Velvet Drift.

What We’re Looking For
Format: Static images + short GIF animations (3–8 seconds)
Platforms: Facebook feed, Instagram feed, Instagram Reels
Style: Modern, aspirational, elegant, clean — with a premium feel
Target Audience: Affluent men and women, ages 50+, health-conscious, looking for ways to support memory and brain health and people concerned or worried that they’re losing their memory and aren’t thinking as quickly or crisply as they want,

Creative Direction
Show Velvet Drift as a premium lifestyle product (not medical or clinical in look).
Think high-end wellness meets cutting-edge science.
Use strong visual hooks: elegant bedside setups, active seniors, subtle cues to scents and sleep, calming colors.
Text overlays should be minimal and impactful.

Tone of Voice (for ad copy in the designs)
Aspirational yet credible
Warm, trustworthy, and empowering
Avoid fear tactics or overpromising

Approved Messaging
✅ Velvet Drift improves memory while you sleep
✅ Clinically backed & drug-free
✅ Simple, effortless nightly use
✅ No RX, no side effects
✅ Elegant bedside design
✅ Improves your mood
✅ Feel Younger
✅ Developed by a top 2% scientist in the world (Caldermoor School of Medicine Study)
✅ 226% memory improvement in seniors
✅ 300% memory improvement in dementia patients

Do NOT Say
❌ Cures Alzheimer’s or dementia
❌ Guaranteed results
❌ Any medical claims beyond memory improvement and cognition support

Deliverables
2+ static ad concepts (1080x1080 + 1080x1920 formats)
1+ short GIF ad concepts (3–8 seconds, loopable)
Layered source files (PSD/AI) preferred

What We’ll Provide You
Our website for reference: www.velvetdrift-example.com
Brand guidelines (logo, colors, fonts)
Approved copy lines and scientific references
Device imagery (with logo placement guidelines)

What We Want to See in Your Work
Unique and scroll-stopping ad ideas (not cookie-cutter templates)
Clever ways to communicate memory improvement + science through visuals
A mix of direct product focus AND lifestyle storytelling

Inspiration
Think of Quillo, Tesvi Band, or Brantel level of sleekness—premium, modern, aspirational.

⚡ Your mission: Help us tell the world about the first device that can improve memory while you sleep—with ads so compelling people can’t scroll past.

```html
<!DOCTYPE html>
<html lang="en">
<head>
<meta charset="UTF-8">
<title>Velvet Drift – Social Ads</title>
<link rel="stylesheet" href="https://fonts.googleapis.com/css2?family=Outfit:wght@300;400;500;600&display=swap">
<style>
  :root {
    --canvas: #fdf0e4;
    --espresso: #2c1a0e;
    --cocoa: #3b2113;
    --sand: #c9a68c;
    --taupe: #a88877;
    --mauve: #7a5b50;
    --device-shade: #8f8379;
    --device-light: #f4d6b8;
    --copper: #b06a4a;
    --cream: #fff6ee;
    --ink: #3a1f12;
    --ink-soft: #4e3123;
  }
  * { margin: 0; padding: 0; box-sizing: border-box; }
  html, body {
    width: 1200px; height: 1000px; overflow: hidden;
    background: var(--canvas);
    font-family: "Outfit", sans-serif;
  }
  .stage { position: relative; width: 1200px; height: 1000px; }

  .ad {
    position: absolute;
    width: 415px;
    overflow: hidden;
    background: linear-gradient(180deg, var(--espresso) 0%, #4a2e1d 22%, var(--sand) 52%, var(--taupe) 68%, var(--mauve) 88%, var(--mauve) 100%);
    box-shadow: 8px 10px 16px rgba(60, 35, 20, 0.35);
  }
  .ad--square { left: 143px; top: 292px; height: 415px; }
  .ad--story { left: 641px; top: 130px; height: 740px; }

  .ad__scene {
    position: absolute; left: 0; width: 100%;
    background:
      radial-gradient(ellipse 40% 22% at 72% 34%, rgba(196, 120, 80, 0.55), transparent 70%),
      radial-gradient(ellipse 60% 40% at 75% 55%, rgba(248, 228, 212, 0.75), transparent 75%),
      linear-gradient(180deg, transparent 0%, rgba(120, 78, 50, 0.5) 18%, rgba(214, 180, 150, 0.55) 60%, transparent 100%);
  }
  .ad--square .ad__scene { top: 60px; height: 290px; }
  .ad--story .ad__scene { top: 130px; height: 450px; }

  .product-shot {
    position: absolute;
    border-radius: 8px 8px 14px 14px;
    background:
      linear-gradient(90deg, var(--device-shade) 0%, #b3a395 55%, var(--device-light) 78%, #e9c7a6 100%);
    border-bottom: 4px solid var(--copper);
    box-shadow: 0 10px 18px rgba(60, 35, 20, 0.3);
  }
  .ad--square .product-shot { left: 40px; top: 95px; width: 138px; height: 212px; }
  .ad--story .product-shot { left: 46px; top: 160px; width: 152px; height: 234px; }

  .brand {
    position: absolute; left: 0; width: 100%;
    text-align: center; color: var(--cream);
    font-weight: 300; letter-spacing: 0.12em; text-transform: uppercase;
    line-height: 1.05;
  }
  .ad--square .brand { top: 19px; font-size: 17px; }
  .ad--story .brand { top: 80px; font-size: 25px; }

  .headline {
    position: absolute; color: var(--ink);
    font-weight: 600; text-align: right; letter-spacing: -0.01em;
  }
  .ad--square .headline { right: 15px; top: 196px; font-size: 27px; line-height: 31px; }
  .ad--story .headline { right: 38px; top: 274px; font-size: 41px; line-height: 50px; }

  .stats { position: absolute; display: flex; color: var(--ink-soft); }
  .stat { text-align: center; }
  .stat__value { display: block; color: var(--ink); font-weight: 600; }
  .stat__label { display: block; font-weight: 300; white-space: nowrap; }

  .ad--square .stats { left: 170px; top: 279px; }
  .ad--square .stat { width: 58px; }
  .ad--square .stat:nth-child(2) { width: 100px; border-left: 1px solid rgba(80, 50, 35, 0.25); border-right: 1px solid rgba(80, 50, 35, 0.25); }
  .ad--square .stat:nth-child(3) { width: 90px; }
  .ad--square .stat__value { font-size: 17px; line-height: 20px; }
  .ad--square .stat__label { font-size: 11px; margin-top: 3px; }

  .ad--story .stats { left: 23px; top: 498px; }
  .ad--story .stat { width: 120px; }
  .ad--story .stat:nth-child(2) { width: 96px; }
  .ad--story .stat:nth-child(3) { width: 140px; }
  .ad--story .stat__value { font-size: 25px; line-height: 30px; }
  .ad--story .stat__label { font-size: 15px; margin-top: 1px; }

  .cta {
    position: absolute; left: 50%; transform: translateX(-50%);
    display: flex; align-items: center; justify-content: center;
    background: var(--cocoa); color: var(--cream);
    border-radius: 999px; font-weight: 400; letter-spacing: 0.02em;
  }
  .ad--square .cta { top: 353px; width: 110px; height: 29px; font-size: 11px; margin-left: -3px; }
  .ad--story .cta { top: 588px; width: 137px; height: 37px; font-size: 14px; }

  .site-url {
    position: absolute; left: 0; width: 100%;
    text-align: center; color: var(--cream); font-weight: 400;
  }
  .ad--square .site-url { top: 386px; font-size: 9.5px; margin-left: -3px; }
  .ad--story .site-url { top: 627px; font-size: 12.5px; }
</style>
</head>
<body>
<main class="stage">

  <section class="ad ad--square" aria-label="Square feed ad">
    <div class="ad__scene" role="img" aria-label="A woman sleeping peacefully in a warm-lit bed with soft scent wisps"></div>
    <div class="product-shot" role="img" aria-label="Velvet Drift bedside scent device, taupe body with copper trim"></div>
    <div class="brand">Velvet<br>Drift</div>
    <h1 class="headline">Better Memory<br>Starts Tonight</h1>
    <div class="stats">
      <div class="stat"><span class="stat__value">0</span><span class="stat__label">Pills</span></div>
      <div class="stat"><span class="stat__value">0</span><span class="stat__label">Side Effects</span></div>
      <div class="stat"><span class="stat__value">100%</span><span class="stat__label">Effortless</span></div>
    </div>
    <div class="cta">BUY NOW</div>
    <p class="site-url">www.velvetdrift-example.com</p>
  </section>

  <section class="ad ad--story" aria-label="Vertical story ad">
    <div class="ad__scene" role="img" aria-label="A woman sleeping peacefully in a warm-lit bed with soft scent wisps"></div>
    <div class="product-shot" role="img" aria-label="Velvet Drift bedside scent device, taupe body with copper trim"></div>
    <div class="brand">Velvet<br>Drift</div>
    <h1 class="headline">Better<br>Memory<br>Starts<br>Tonight</h1>
    <div class="stats">
      <div class="stat"><span class="stat__value">0</span><span class="stat__label">Pills</span></div>
      <div class="stat"><span class="stat__value">0</span><span class="stat__label">Side Effects</span></div>
      <div class="stat"><span class="stat__value">100%</span><span class="stat__label">Effortless</span></div>
    </div>
    <div class="cta">BUY NOW</div>
    <p class="site-url">www.velvetdrift-example.com</p>
  </section>

</main>
</body>
</html>
```